Healthcare IT company looking for business card design

We develop IT systems for healthcare that significantly reduces cost and improves quality.

We want a business card design that is professional and clean, and using the colors in our logo.

Target Market(s)

Doctors and decision makers in the healthcare industry

Industry/Entity Type

Healthcare

Contact Information for Business Card

It should include
Name and title, address, telephone

Tobias Vrenholt, CEO
+46 712 418257
tobias@kelvaro.se

Font styles to use
Serif

Colors
0355a3
ed282f

Requirements
Must have
• Clean design
• Professional feel
Nice to have
• N/A
Should not have
• N/A

```html
<!DOCTYPE html>
<html lang="en">
<head>
<meta charset="utf-8">
<title>Kelvaro business card</title>
<link href="https://fonts.googleapis.com/css2?family=Arimo:wght@400;700&display=swap" rel="stylesheet">
<style>
  :root {
    --brand-blue: #0355a3;
    --card-blue: #1c5fae;
    --brand-red: #ed282f;
    --paper: #f2f2f2;
    --paper-shade: #dedede;
    --backdrop: #2b2b2b;
    --ink-light: #e8eef7;
  }
  * { margin: 0; padding: 0; box-sizing: border-box; }
  html, body { width: 1200px; height: 997px; overflow: hidden; }
  body {
    background: var(--backdrop);
    font-family: "Arimo", Arial, sans-serif;
    position: relative;
  }
  .card {
    position: absolute;
    left: 320px;
    width: 560px;
    height: 320px;
    border-radius: 18px;
    overflow: hidden;
    background: var(--card-blue);
    box-shadow: 0 14px 30px rgba(0,0,0,.5);
  }
  .card-front { top: 110px; }
  .card-back { top: 520px; }
  .card-shapes { position: absolute; inset: 0; }
  .front-brand {
    position: absolute;
    left: 0; right: 0; top: 110px;
    text-align: center;
    color: #fff;
  }
  .front-brand .wordmark {
    font-size: 70px; font-weight: 700; letter-spacing: 1px;
    display: inline-flex; align-items: center; gap: 12px;
  }
  .mark-dot {
    width: 18px; height: 18px; border-radius: 50%;
    background: var(--brand-red); display: inline-block;
  }
  .front-brand .web {
    font-size: 17px; letter-spacing: 6px; margin-top: 4px;
  }
  .back-brand {
    position: absolute; left: 44px; top: 120px;
    color: var(--brand-blue);
    font-size: 56px; font-weight: 700;
    display: flex; align-items: center; gap: 10px;
  }
  .back-address {
    position: absolute; left: 44px; bottom: 36px;
    font-weight: 700;
  }
  .back-address .company { color: var(--brand-red); font-size: 18px; }
  .back-address .street { color: var(--brand-blue); font-size: 15px; margin-top: 2px; }
  .person {
    position: absolute; left: 362px; right: 18px; top: 56px;
    text-align: center; color: var(--ink-light);
  }
  .person .name { font-size: 21px; white-space: nowrap; }
  .person .title { font-size: 12px; margin-top: 4px; }
  .contact {
    position: absolute; right: 26px; bottom: 40px;
    color: var(--ink-light); font-size: 13px; text-align: right;
  }
  .contact li { list-style: none; display: flex; align-items: center; justify-content: flex-end; gap: 6px; margin-top: 10px; }
  .contact svg { width: 16px; height: 16px; }
</style>
</head>
<body>

<section class="card card-front">
  <svg class="card-shapes" viewBox="0 0 560 320" preserveAspectRatio="none" aria-hidden="true">
    <polygon points="0,0 70,0 0,200" fill="var(--paper)"/>
    <polygon points="470,320 560,320 560,70" fill="var(--paper)"/>
  </svg>
  <div class="front-brand">
    <div class="wordmark"><span>Kelvaro</span><span class="mark-dot"></span></div>
    <div class="web">www.kelvaro.se</div>
  </div>
</section>

<section class="card card-back">
  <svg class="card-shapes" viewBox="0 0 560 320" preserveAspectRatio="none" aria-hidden="true">
    <defs>
      <linearGradient id="paperFade" x1="0" y1="0" x2="1" y2="1">
        <stop offset="0" stop-color="var(--paper)"/>
        <stop offset="1" stop-color="var(--paper-shade)"/>
      </linearGradient>
    </defs>
    <polygon points="0,0 360,0 290,320 0,320" fill="url(#paperFade)"/>
  </svg>
  <div class="back-brand"><span>Kelvaro</span><span class="mark-dot"></span></div>
  <div class="back-address">
    <div class="company">Kelvaro Pvt Ltd</div>
    <div class="street">18th &amp; Maple Row, Canada</div>
  </div>
  <div class="person">
    <div class="name">Tobias Vrenholt</div>
    <div class="title">CEO</div>
  </div>
  <ul class="contact">
    <li>+46 712 418257
      <svg viewBox="0 0 16 16" aria-hidden="true"><rect width="16" height="16" rx="4" fill="var(--brand-red)"/><path d="M4 5.5c0-1 1-1.8 4-1.8s4 .8 4 1.8v1h-2.2v-1H6.2v1H4z M5 8h6l1 4H4z" fill="#fff"/></svg>
    </li>
    <li>tobias@kelvaro.se
      <svg viewBox="0 0 16 16" aria-hidden="true"><rect width="16" height="16" rx="4" fill="var(--brand-red)"/><path d="M6 10l4-4M7.5 4.5l1-1a2 2 0 0 1 3 3l-1 1M8.5 11.5l-1 1a2 2 0 0 1-3-3l1-1" stroke="#fff" stroke-width="1.4" fill="none" stroke-linecap="round"/></svg>
    </li>
  </ul>
</section>

</body>
</html>
```